I'm an Executive Coach. I need a cover for a leadership book.

Title: Quiet Compass Wide Horizon Guidance from the Center of the Spirit. The focus in my work "Soul Woven Purpose" I use a lot of fire and heart-centered frame work and imagery. The book should have a leadership presence with an inspirational feel. The purpose is to invite really smart leaders to pay attention and to lead from their heart so they can have great impact in the work they do and the lives they live. priyalangford.example to see site branding, colors. Author: Priya Langford

Target Market(s)

The audience is those lead others from the manager level to the executive level and entrepreneurs starting and leading their own companies They are usually trailblazers, care about connecting with people as they lead. The big message is being confifent to lead ftom values, intention and from what matters most.

Industry/Entity Type

Executive coaching

Font styles to use
Serif

Requirements
Must have
• Lighter feel. Perhaps avoid a total black background.
Nice to have
• While it is a leadership book, i would like it to feel creative and inviting not authoritative.
Should not have
• Dark colors as the main color

```html
<!DOCTYPE html>
<html lang="en">
<head>
<meta charset="utf-8">
<title>Quiet Compass Wide Horizon Guidance — Priya Langford</title>
<link rel="stylesheet" href="https://fonts.googleapis.com/css2?family=Cinzel:wght@400;500&family=Great+Vibes&display=swap">
<style>
  :root {
    --red-edge: #b50e12;
    --red-mid: #d41518;
    --red-bright: #ec2a1e;
    --red-glow: #ff3a26;
    --ember: #f5641e;
    --core: #ffd826;
    --ink-light: #ffffff;
  }
  html, body {
    margin: 0;
    padding: 0;
    width: 811px;
    height: 1200px;
    overflow: hidden;
    background: var(--red-mid);
  }
  .cover {
    position: relative;
    width: 811px;
    height: 1200px;
    overflow: hidden;
    background:
      radial-gradient(ellipse 220px 160px at 50% 0%, rgba(255, 50, 35, 0.9), rgba(255, 50, 35, 0) 100%),
      radial-gradient(ellipse 700px 900px at 50% 70%, var(--red-bright) 0%, var(--red-mid) 55%, var(--red-edge) 100%);
  }
  .heart-glow {
    position: absolute;
    left: 0;
    top: 600px;
    width: 811px;
    height: 560px;
    background:
      radial-gradient(circle 26px at 50% 49%, var(--core) 0%, rgba(255, 180, 30, 0.9) 60%, rgba(245, 100, 30, 0) 100%),
      radial-gradient(ellipse 120px 110px at 50% 48%, rgba(245, 100, 30, 0.9) 0%, rgba(236, 42, 30, 0.6) 55%, rgba(236, 42, 30, 0) 100%),
      radial-gradient(ellipse 340px 280px at 50% 46%, rgba(255, 58, 38, 0.5) 0%, rgba(236, 42, 30, 0) 100%);
  }
  .title {
    position: absolute;
    left: 0;
    top: 86px;
    width: 811px;
    margin: 0;
    text-align: center;
    font-family: "Cinzel", serif;
    font-weight: 400;
    font-size: 114px;
    line-height: 109px;
    color: var(--ink-light);
    letter-spacing: 1px;
  }
  .title span { display: block; }
  .subtitle {
    position: absolute;
    left: 0;
    top: 636px;
    width: 811px;
    margin: 0;
    text-align: center;
    font-family: "Cinzel", serif;
    font-weight: 500;
    font-size: 32px;
    letter-spacing: 1px;
    color: var(--ink-light);
  }
  .author {
    position: absolute;
    left: 0;
    top: 1010px;
    width: 811px;
    margin: 0;
    text-align: center;
    font-family: "Great Vibes", cursive;
    font-weight: 400;
    font-size: 104px;
    line-height: 130px;
    color: var(--ink-light);
  }
</style>
</head>
<body>
  <main class="cover">
    <div class="heart-glow" role="img" aria-label="Concentric red hearts radiating from a glowing golden center"></div>
    <h1 class="title">
      <span>Quiet</span>
      <span>Compass</span>
      <span>Wide</span>
      <span>Horizon</span>
      <span>Guidance</span>
    </h1>
    <p class="subtitle">from the Center of the Spirit</p>
    <p class="author">Priya Langford</p>
  </main>
</body>
</html>
```